Visitenkarten-Design
Zielgruppe
Malerbetrieb
Zielgruppe: Private Haushalte, Hausverwaltungen
Aufgabenstellung
Logo ist vorhanden
Lorenz Dallmer
Malermeister

```html
<!DOCTYPE html>
<html lang="de">
<head>
<meta charset="utf-8">
<title>Visitenkarte Malereibetrieb Dallmer</title>
<link rel="stylesheet" href="https://fonts.googleapis.com/css2?family=Inter:ital,wght@0,300;0,400;0,700;1,400&family=Open+Sans:wght@400&display=swap">
<style>
  :root {
    --page-bg: #eeeef0;
    --card-white: #ffffff;
    --ink: #2b2b2d;
    --ink-soft: #7a7a7c;
    --cyan: #079fe0;
    --yellow: #fbea12;
    --magenta: #e2198a;
    --charcoal: #363636;
  }
  html, body {
    margin: 0;
    padding: 0;
    width: 1200px;
    height: 1095px;
    overflow: hidden;
    background: var(--page-bg);
  }
  .canvas {
    position: relative;
    width: 1200px;
    height: 1095px;
    font-family: "Inter", Arial, sans-serif;
    color: var(--ink);
  }
  .card {
    position: absolute;
    width: 390px;
    height: 602px;
  }
  .card--front {
    left: 186px;
    top: 106px;
    background: var(--card-white);
  }
  .card--back {
    left: 626px;
    top: 428px;
    background: linear-gradient(150deg, var(--cyan) 0%, var(--yellow) 42%, var(--magenta) 78%, var(--charcoal) 100%);
  }
  .brand {
    position: absolute;
    left: 20px;
    top: 249px;
    width: 220px;
  }
  .brand__name {
    display: flex;
    align-items: center;
    gap: 10px;
    font-weight: 700;
    font-size: 46px;
    line-height: 54px;
    letter-spacing: 0.5px;
    color: var(--ink);
  }
  .brand__square {
    width: 14px;
    height: 14px;
    background: var(--ink);
  }
  .brand__trade {
    margin-top: 4px;
    font-weight: 300;
    font-size: 23px;
    line-height: 24px;
    letter-spacing: 0.2px;
    color: var(--ink);
  }
  .brand__claim {
    margin-top: 3px;
    font-family: "Open Sans", Arial, sans-serif;
    font-size: 12.5px;
    line-height: 15px;
    color: var(--ink-soft);
  }
  .person {
    position: absolute;
    left: 20px;
    top: 404px;
  }
  .person__name {
    margin: 0;
    font-weight: 700;
    font-size: 27px;
    line-height: 30px;
    letter-spacing: 0.3px;
  }
  .person__role {
    margin: 0;
    font-style: italic;
    font-size: 20px;
    line-height: 26px;
    letter-spacing: 1.2px;
  }
  .contact {
    position: absolute;
    left: 20px;
    top: 484px;
    margin: 0;
    font-size: 20px;
    line-height: 25px;
    font-weight: 400;
  }
  .contact__row {
    display: flex;
  }
  .contact__label {
    width: 18px;
    font-size: 11px;
    font-weight: 700;
    line-height: 14px;
  }
</style>
</head>
<body>
  <main class="canvas">
    <section class="card card--front" aria-label="Vorderseite">
      <div class="brand">
        <div class="brand__name"><span>DALLMER</span><span class="brand__square"></span></div>
        <div class="brand__trade">MALEREIBETRIEB</div>
        <div class="brand__claim">Sorgfalt in jedem Pinselstrich</div>
      </div>
      <div class="person">
        <p class="person__name">LORENZ DALLMER</p>
        <p class="person__role">MALERMEISTER</p>
      </div>
      <dl class="contact">
        <div class="contact__row"><span class="contact__label">A</span><span>Lindenkamp 114 B</span></div>
        <div class="contact__row"><span class="contact__label"></span><span>22147 Hamburg</span></div>
        <div class="contact__row"><span class="contact__label">T</span><span>0176 48 21 539</span></div>
        <div class="contact__row"><span class="contact__label">E</span><span>info@malereibetrieb-dallmer.de</span></div>
      </dl>
    </section>

    <section class="card card--back" role="img" aria-label="Rückseite mit farbiger Flächengrafik in Cyan, Gelb, Magenta und Anthrazit"></section>
  </main>
</body>
</html>
```